Flenzo Thumbnail for Educational Video About KR9

Please design a bespoke thumbnail for a Flenzo video with the following title:
"Nobody Expected What Came Over That Ridge"
The video is about the battle for Castle Brunok, which was a small battle that happened during KR9, in which the Germans fought against themselves for control of Castle Brunok.
The thumbnail should be 1920x1080 pixels

```html
<!DOCTYPE html>
<html lang="en">
<head>
<meta charset="utf-8">
<title>Flenzo – Nobody Expected What Came Over That Ridge</title>
<link rel="stylesheet" href="https://fonts.googleapis.com/css2?family=Teko:wght@600&family=Roboto+Condensed:ital,wght@0,400;0,700;1,400&display=swap">
<style>
  :root {
    --page-bg: #e4e4e4;
    --card-bg: #f7f7f7;
    --ink: #2b2b2b;
    --ink-soft: #555555;
    --ink-faint: #9a9a9a;
    --headline-white: #ffffff;
    --headline-yellow: #fff200;
    --accent-red: #e8474a;
    --progress-red: #f0444a;
    --track: #d9d9d9;
    --scene-light: #e07a80;
    --scene-rose: #b8454f;
    --scene-mid: #7a1e28;
    --scene-dark: #3a0d12;
    --scene-black: #0d0b0b;
    --rule: #3a3a3a;
    --icon-hole: #111111;
  }
  * { box-sizing: border-box; margin: 0; padding: 0; }
  html, body { width: 1200px; height: 900px; overflow: hidden; }
  body { background: var(--page-bg); font-family: "Roboto Condensed", Arial, sans-serif; position: relative; }

  .video-card {
    position: absolute; left: 150px; top: 70px; width: 900px; height: 740px;
    background: var(--card-bg);
  }
  .player {
    position: absolute; left: 30px; top: 30px; width: 840px; height: 472px; overflow: hidden;
    background: var(--scene-black);
  }
  .scene-art {
    position: absolute; left: 0; top: 0; width: 840px; height: 380px;
    background:
      radial-gradient(ellipse 45% 55% at 70% 20%, var(--scene-light) 0%, rgba(224,122,128,0) 100%),
      linear-gradient(160deg, var(--scene-mid) 0%, var(--scene-rose) 45%, var(--scene-mid) 70%, var(--scene-dark) 100%);
  }
  .scene-fade {
    position: absolute; left: 0; right: 0; top: 200px; bottom: 0;
    background: linear-gradient(180deg, rgba(13,11,11,0) 0%, rgba(13,11,11,0.75) 45%, var(--scene-black) 85%);
  }
  .headline {
    position: absolute; left: 36px; top: 236px;
    font-family: "Teko", "Arial Narrow", sans-serif; font-weight: 600;
    font-size: 78px; line-height: 64px; letter-spacing: 1px; text-transform: uppercase;
  }
  .headline-line { display: block; color: var(--headline-white); }
  .headline-line--accent { color: var(--headline-yellow); }

  .progress { position: absolute; left: 28px; right: 34px; top: 432px; height: 4px; background: var(--track); }
  .progress-played { position: absolute; left: 0; top: 0; width: 42%; height: 100%; background: var(--progress-red); }
  .progress-knob { position: absolute; left: calc(42% - 6px); top: -4px; width: 12px; height: 12px; border-radius: 50%; background: var(--progress-red); }

  .controls { position: absolute; left: 28px; right: 34px; top: 446px; height: 20px; display: flex; align-items: center; color: var(--headline-white); }
  .controls svg { fill: var(--headline-white); }
  .controls-left, .controls-right { display: flex; align-items: center; gap: 14px; }
  .controls-right { margin-left: auto; gap: 20px; }
  .volume-track { width: 44px; height: 3px; background: var(--headline-white); position: relative; }
  .volume-track::after { content: ""; position: absolute; right: -4px; top: -4px; width: 10px; height: 10px; border-radius: 50%; background: var(--headline-white); }
  .timecode { font-size: 13px; font-style: italic; margin-left: 8px; }

  .video-title { position: absolute; left: 40px; top: 532px; font-size: 18px; color: var(--ink); }
  .view-count { position: absolute; left: 40px; top: 558px; font-size: 11px; font-style: italic; color: var(--ink-faint); }

  .actions { position: absolute; right: 40px; top: 584px; display: flex; align-items: center; gap: 26px; font-size: 14px; color: var(--ink-soft); text-transform: uppercase; }
  .action { display: flex; align-items: center; gap: 5px; }
  .action svg { fill: var(--ink); }

  .divider { position: absolute; left: 40px; right: 40px; top: 620px; height: 2px; background: var(--rule); }

  .channel { position: absolute; left: 50px; top: 642px; display: flex; align-items: center; gap: 22px; }
  .channel-avatar { width: 60px; height: 60px; border-radius: 50%; background: var(--ink); }
  .channel-name { font-weight: 700; font-size: 17px; color: var(--ink-soft); }
  .channel-subs { font-size: 12px; font-style: italic; color: var(--ink-faint); margin-top: 6px; }

  .subscribe {
    position: absolute; right: 60px; top: 662px; width: 160px; height: 40px;
    background: var(--accent-red); color: #fff; font-size: 18px;
    display: flex; align-items: center; justify-content: center; text-transform: uppercase;
  }
</style>
</head>
<body>
  <article class="video-card">
    <div class="player">
      <div class="scene-art" role="img" aria-label="Painted battle scene in deep red: a castle with flags on a hill, pine forest, soldiers and a tank beneath a smoky sky with birds"></div>
      <div class="scene-fade"></div>
      <h1 class="headline">
        <span class="headline-line">Nobody Expected</span>
        <span class="headline-line headline-line--accent">What Came Over</span>
        <span class="headline-line">That Ridge</span>
      </h1>
      <div class="progress"><div class="progress-played"></div><div class="progress-knob"></div></div>
      <div class="controls">
        <div class="controls-left">
          <svg width="14" height="16" viewBox="0 0 14 16"><path d="M1 1 L13 8 L1 15 Z"/></svg>
          <svg width="14" height="14" viewBox="0 0 14 14"><path d="M1 1 L9 7 L1 13 Z"/><rect x="10" y="1" width="3" height="12"/></svg>
          <svg width="16" height="14" viewBox="0 0 16 14"><path d="M1 4 H5 L10 0 V14 L5 10 H1 Z"/><path d="M12 4 Q14 7 12 10" stroke="#fff" stroke-width="1.5" fill="none"/></svg>
          <span class="volume-track"></span>
          <span class="timecode">0:50 / 2:50</span>
        </div>
        <div class="controls-right">
          <svg width="20" height="16" viewBox="0 0 20 16"><rect x="0" y="0" width="20" height="16" rx="2"/><rect x="3" y="9" width="6" height="2" fill="#111"/><rect x="11" y="9" width="6" height="2" fill="#111"/><rect x="3" y="12" width="14" height="2" fill="#111"/></svg>
          <svg class="icon-settings" width="18" height="18" viewBox="0 0 18 18">
            <g>
              <rect x="7" y="0.5" width="4" height="4" rx="0.6"/>
              <rect x="7" y="0.5" width="4" height="4" rx="0.6" transform="rotate(45 9 9)"/>
              <rect x="7" y="0.5" width="4" height="4" rx="0.6" transform="rotate(90 9 9)"/>
              <rect x="7" y="0.5" width="4" height="4" rx="0.6" transform="rotate(135 9 9)"/>
              <rect x="7" y="0.5" width="4" height="4" rx="0.6" transform="rotate(180 9 9)"/>
              <rect x="7" y="0.5" width="4" height="4" rx="0.6" transform="rotate(225 9 9)"/>
              <rect x="7" y="0.5" width="4" height="4" rx="0.6" transform="rotate(270 9 9)"/>
              <rect x="7" y="0.5" width="4" height="4" rx="0.6" transform="rotate(315 9 9)"/>
            </g>
            <circle cx="9" cy="9" r="6"/>
            <circle cx="9" cy="9" r="2.4" fill="#111"/>
          </svg>
          <svg width="22" height="16" viewBox="0 0 22 16"><rect x="1" y="1" width="20" height="14" rx="2" fill="none" stroke="#fff" stroke-width="2"/><rect x="11" y="8" width="7" height="5"/></svg>
          <svg width="24" height="16" viewBox="0 0 24 16"><rect x="1" y="2" width="22" height="12" fill="none" stroke="#fff" stroke-width="2"/></svg>
          <svg width="22" height="18" viewBox="0 0 22 18"><path d="M1 4 V2 H21 V16 H13" fill="none" stroke="#fff" stroke-width="2"/><path d="M1 8 A9 9 0 0 1 10 17 M1 12 A5 5 0 0 1 6 17" fill="none" stroke="#fff" stroke-width="2"/></svg>
          <svg width="18" height="18" viewBox="0 0 18 18"><path d="M1 6 V1 H6 M12 1 H17 V6 M17 12 V17 H12 M6 17 H1 V12" fill="none" stroke="#fff" stroke-width="2.5"/></svg>
        </div>
      </div>
    </div>

    <p class="video-title">Nobody Expected What Came Over That Ridge | KR9 - Castle Brunok</p>
    <p class="view-count">35,064,099 views</p>

    <div class="actions">
      <span class="action"><svg width="16" height="16" viewBox="0 0 16 16"><rect x="0" y="6" width="4" height="10"/><path d="M5 6 L9 0 Q11 0 10.5 3 L10 6 H15 Q16 7 15.5 8 L13 15 Q12.5 16 11 16 H5 Z"/></svg>Like</span>
      <span class="action"><svg width="16" height="16" viewBox="0 0 16 16"><g transform="rotate(180 8 8)"><rect x="0" y="6" width="4" height="10"/><path d="M5 6 L9 0 Q11 0 10.5 3 L10 6 H15 Q16 7 15.5 8 L13 15 Q12.5 16 11 16 H5 Z"/></g></svg>Dislike</span>
      <span class="action"><svg width="18" height="14" viewBox="0 0 18 14"><path d="M10 0 L18 6 L10 12 V8 Q3 8 0 14 Q1 5 10 4 Z"/></svg>Share</span>
      <span class="action"><svg width="18" height="14" viewBox="0 0 18 14"><rect x="0" y="1" width="11" height="2"/><rect x="0" y="6" width="11" height="2"/><rect x="0" y="11" width="7" height="2"/><rect x="13" y="6" width="2" height="8"/><rect x="10" y="9" width="8" height="2"/></svg>Save</span>
      <span class="action"><svg width="22" height="6" viewBox="0 0 22 6"><circle cx="3" cy="3" r="2.5"/><circle cx="11" cy="3" r="2.5"/><circle cx="19" cy="3" r="2.5"/></svg></span>
    </div>

    <div class="divider"></div>

    <div class="channel">
      <div class="channel-avatar"></div>
      <div>
        <p class="channel-name">Archive Fronts</p>
        <p class="channel-subs">11.4M subscribers</p>
      </div>
    </div>

    <div class="subscribe">Subscribe</div>
  </article>
</body>
</html>
```